Luxury Candle Startup Needs Modern Packaging Box & Matching Label Design

We are Lunavale, a luxury candle company about to launch in Australia and we need a box packaging design that is modern, minimalist, and feminine. Our target audience are females, mostly mothers, within the age range of 25-45 who are looking for high quality, handmade luxurious products. Our company is going to have a large social media presence with new mothers as we are going to show our journey with starting a business whilst on maternity leave. We would like the arch shape incorporated into the box packaging as it is beautiful and symbolises moving into a new phase in life which really represents the brand. We would like for the packaging box to be a simple white box with a sleeve insert over the box with the design to make printing easier. Our colour inspiration are very earthy colours and would like the sleeve colour to be easily changed according to the scent. For example dusky rose coloured sleeve for rose patchouli and amber scent, light coffee coloured sleeve for coffee bean cacao scent etc. Please see uploaded files for inspiration, our logo, and the type of candle jars used.
The box dimensions are:
External Dimension: 95mmW x 95mmL x 116mmH
We look forward to seeing your amazing designs!

```html
<!DOCTYPE html>
<html lang="en">
<head>
<meta charset="UTF-8">
<title>Lunavale – Autumn Sleeve &amp; Label</title>
<link rel="stylesheet" href="https://fonts.googleapis.com/css2?family=Jost:wght@300;400;500&display=swap">
<style>
  :root {
    --stage: #f2f2f2;
    --sand: #c1b193;
    --sleeve-base: #bcae92;
    --rust: #9c4a3a;
    --rust-soft: #c98a78;
    --umber: #3a2a24;
    --brand-brown: #7a5a4b;
    --scent-brown: #8a7560;
    --white: #ffffff;
    --box-white: #fbfbfb;
  }
  * { box-sizing: border-box; margin: 0; padding: 0; }
  html, body { width: 1200px; height: 1200px; overflow: hidden; }
  body {
    background: var(--stage);
    font-family: "Jost", "Helvetica Neue", Arial, sans-serif;
    position: relative;
  }

  .artwork-area {
    position: absolute; left: 0; top: 0;
    width: 1200px; height: 872px;
  }

  /* Box with sleeve, flat front view */
  .box-front {
    position: absolute;
    left: 330px; top: 220px;
    width: 400px; height: 490px;
    background: var(--box-white);
    box-shadow: 0 0 0 1px #e4e4e4;
  }
  .sleeve {
    position: absolute;
    left: 40px; top: 0;
    width: 320px; height: 490px;
    overflow: hidden;
  }
  .sleeve-art, .label-art {
    position: absolute; inset: 0;
    background:
      radial-gradient(ellipse 35% 22% at 78% 22%, rgba(156,74,58,.85), transparent 70%),
      radial-gradient(ellipse 30% 20% at 72% 55%, rgba(120,50,40,.8), transparent 70%),
      radial-gradient(ellipse 28% 26% at 30% 48%, rgba(58,42,36,.55), transparent 70%),
      radial-gradient(ellipse 30% 18% at 20% 12%, rgba(201,138,120,.7), transparent 70%),
      radial-gradient(ellipse 22% 16% at 12% 42%, rgba(156,74,58,.7), transparent 70%),
      var(--sleeve-base);
  }
  .sleeve-lockup {
    position: absolute;
    left: 0; right: 0; top: 160px;
    text-align: center;
    color: var(--white);
  }
  .sleeve-scent {
    position: absolute;
    left: 0; right: 0; bottom: 42px;
    text-align: center;
    font-weight: 300;
    font-size: 17px;
    letter-spacing: 1px;
    color: var(--scent-brown);
  }

  /* Arch swing label */
  .arch-label {
    position: absolute;
    left: 830px; top: 380px;
    width: 160px; height: 292px;
    border-radius: 80px 80px 0 0;
    overflow: hidden;
  }
  .label-lockup {
    position: absolute;
    left: 0; right: 0; bottom: 12px;
    text-align: center;
    color: var(--white);
  }

  /* Shared lockup type */
  .wordmark {
    font-weight: 400;
    text-transform: uppercase;
    letter-spacing: 2px;
    line-height: 1;
  }
  .tagline {
    font-weight: 500;
    text-transform: uppercase;
    letter-spacing: 2px;
    line-height: 1;
  }
  .sleeve-lockup .wordmark { font-size: 38px; }
  .sleeve-lockup .tagline.primary { font-size: 8px; margin-top: 10px; }
  .sleeve-lockup .tagline.secondary { font-size: 6px; margin-top: 7px; }
  .label-lockup .wordmark { font-size: 20px; letter-spacing: 1px; }
  .label-lockup .tagline.primary { font-size: 7px; margin-top: 7px; }
  .label-lockup .tagline.secondary { font-size: 5px; margin-top: 6px; }

  /* Brand band */
  .brand-band {
    position: absolute;
    left: 0; top: 872px;
    width: 1200px; height: 328px;
    background: var(--sand);
  }
  .band-lockup {
    position: absolute;
    left: 0; right: 0; top: 94px;
    text-align: center;
    color: var(--brand-brown);
  }
  .band-lockup .wordmark { font-size: 46px; letter-spacing: 4px; }
  .band-lockup .tagline.primary { font-size: 10px; margin-top: 20px; letter-spacing: 2.5px; }
  .band-lockup .tagline.secondary { font-size: 8px; margin-top: 9px; letter-spacing: 2px; }
  .band-lockup .scent {
    margin-top: 20px;
    font-weight: 300;
    font-size: 22px;
    letter-spacing: 1px;
    color: var(--scent-brown);
  }
</style>
</head>
<body>
  <section class="artwork-area">
    <div class="box-front">
      <div class="sleeve">
        <div class="sleeve-art" role="img" aria-label="Soft-focus photograph of autumn eucalyptus leaves in rust and deep brown on a sand background"></div>
        <div class="sleeve-lockup">
          <div class="wordmark">Lunavale</div>
          <div class="tagline primary">Luxury Fragrance</div>
          <div class="tagline secondary">Australia</div>
        </div>
        <div class="sleeve-scent">AUTUMN</div>
      </div>
    </div>

    <div class="arch-label">
      <div class="label-art" role="img" aria-label="Soft-focus photograph of autumn eucalyptus leaves in rust and deep brown on a sand background"></div>
      <div class="label-lockup">
        <div class="wordmark">Lunavale</div>
        <div class="tagline primary">Luxury Fragrance</div>
        <div class="tagline secondary">Australia</div>
      </div>
    </div>
  </section>

  <section class="brand-band">
    <div class="band-lockup">
      <div class="wordmark">Lunavale</div>
      <div class="tagline primary">Luxury Fragrance</div>
      <div class="tagline secondary">Australia</div>
      <div class="scent">AUTUMN</div>
    </div>
  </section>
</body>
</html>
```